Christmas Collection Candle Label Design

Looking to update our existing Christmas Candle Collection labels. Labels should reflect the overall feel of our brand- www.wickmerelane.ca
Want to include some color elements. Holiday colors added into design but more muted/ earthy tones not vibrant colors . Metallic elements and line art botanical illustration. Fonts should be more align to brand
Scents
Holiday Tree
Candy Cane
Sugar and Spice
Joyeaux Noel

```html
<!DOCTYPE html>
<html lang="en">
<head>
<meta charset="utf-8">
<title>Christmas Collection Candle Labels</title>
<link rel="stylesheet" href="https://fonts.googleapis.com/css2?family=Cormorant+SC:wght@400;500&family=Mrs+Saint+Delafield&display=swap">
<style>
  :root {
    --page: #ffffff;
    --paper: #f2efe7;
    --sage: #8d917a;
    --rose: #cf9584;
    --gold-band: #bb9f6e;
    --berry: #bd5f5c;
    --gold-dark: #9a7a45;
    --gold-light: #eadb9f;
    --gold-mid: #c4a564;
    --ink-light: #fbf6e8;
  }
  * { box-sizing: border-box; margin: 0; padding: 0; }
  html, body { width: 1200px; height: 1200px; overflow: hidden; background: var(--page); }
  .sheet { position: relative; width: 1200px; height: 1200px; }

  .label {
    position: absolute;
    width: 357px;
    height: 357px;
    background: var(--paper);
    overflow: hidden;
  }
  .label--noel  { left: 421px; top: 186px; }
  .label--sugar { left: 47px;  top: 694px; }
  .label--tree  { left: 422px; top: 694px; }
  .label--candy { left: 796px; top: 694px; }

  .label__claim {
    position: absolute;
    left: 0; right: 0; top: 13px;
    height: 26px;
    display: flex; align-items: center; justify-content: center;
    font-family: "Cormorant SC", serif;
    font-size: 16px;
    letter-spacing: 0.4px;
    color: var(--ink-light);
  }
  .label--noel  .label__claim { background: var(--sage); }
  .label--sugar .label__claim { background: var(--rose); }
  .label--tree  .label__claim { background: var(--gold-band); }
  .label--candy .label__claim { background: var(--berry); }

  .label__title {
    position: absolute;
    left: 0; right: 0; top: 62px;
    height: 170px;
    font-family: "Mrs Saint Delafield", cursive;
    font-weight: 400;
  }
  .label__word {
    position: absolute;
    font-size: 78px;
    line-height: 1;
    white-space: nowrap;
    background: linear-gradient(100deg, var(--gold-dark) 0%, var(--gold-light) 45%, var(--gold-mid) 70%, var(--gold-dark) 100%);
    -webkit-background-clip: text;
    background-clip: text;
    color: transparent;
  }

  .label__art {
    position: absolute;
    left: 0; right: 0; top: 232px; bottom: 0;
  }
  .label--noel  .label__art { background: linear-gradient(180deg, rgba(141,145,122,0) 0%, rgba(141,145,122,0.45) 60%, rgba(141,145,122,0.55) 100%); }
  .label--sugar .label__art { background: linear-gradient(180deg, rgba(207,149,132,0) 0%, rgba(207,149,132,0.45) 60%, rgba(207,149,132,0.55) 100%); }
  .label--tree  .label__art { background: linear-gradient(180deg, rgba(187,159,110,0) 0%, rgba(187,159,110,0.5) 60%, rgba(187,159,110,0.6) 100%); }
  .label--candy .label__art { background: linear-gradient(180deg, rgba(189,95,92,0) 0%, rgba(189,95,92,0.45) 60%, rgba(189,95,92,0.55) 100%); }

  .label__footer {
    position: absolute;
    left: 0; right: 0; top: 320px;
    height: 25px;
    display: flex; align-items: center; justify-content: center;
    gap: 9px;
    background: linear-gradient(90deg, #a8875a 0%, #c9ad73 25%, #ecdfa8 42%, #c8aa6d 62%, #9c7c4c 85%, #86653d 100%);
    font-family: "Cormorant SC", serif;
    color: var(--ink-light);
    white-space: nowrap;
  }
  .label__origin { font-size: 10.5px; letter-spacing: 0.3px; }
  .label__brand  { font-size: 13px; letter-spacing: 0.3px; }
  .label__weight { font-size: 12px; }
  .label__divider { width: 1px; height: 10px; background: rgba(251,246,232,0.7); }
</style>
</head>
<body>
<main class="sheet">

  <section class="label label--noel">
    <p class="label__claim">Made with plant-based botanicals</p>
    <h2 class="label__title">
      <span class="label__word" style="left:70px; top:8px;">Joyeaux</span>
      <span class="label__word" style="left:128px; top:76px;">Noel</span>
    </h2>
    <div class="label__art" role="img" aria-label="Line-art evergreen sprigs and dotted snow in sage green"></div>
    <div class="label__footer">
      <span class="label__origin">Made in Canada</span><span class="label__divider"></span>
      <span class="label__brand">Wickmere Lane</span><span class="label__divider"></span>
      <span class="label__weight">Net wt. 25 oz | 709 g</span>
    </div>
  </section>

  <section class="label label--sugar">
    <p class="label__claim">Made with plant-based botanicals</p>
    <h2 class="label__title">
      <span class="label__word" style="left:52px; top:12px;">Sugar</span>
      <span class="label__word" style="left:128px; top:78px;">&amp; Spice</span>
    </h2>
    <div class="label__art" role="img" aria-label="Line-art star anise, orange slices and gingerbread figures in dusty rose"></div>
    <div class="label__footer">
      <span class="label__origin">Made in Canada</span><span class="label__divider"></span>
      <span class="label__brand">Wickmere Lane</span><span class="label__divider"></span>
      <span class="label__weight">Net wt. 25 oz | 709 g</span>
    </div>
  </section>

  <section class="label label--tree">
    <p class="label__claim">Made with plant-based botanicals</p>
    <h2 class="label__title">
      <span class="label__word" style="left:58px; top:12px;">Holiday</span>
      <span class="label__word" style="left:176px; top:78px;">Tree</span>
    </h2>
    <div class="label__art" role="img" aria-label="Line-art string of holiday lights and ornaments in antique gold"></div>
    <div class="label__footer">
      <span class="label__origin">Made in Canada</span><span class="label__divider"></span>
      <span class="label__brand">Wickmere Lane</span><span class="label__divider"></span>
      <span class="label__weight">Net wt. 25 oz | 709 g</span>
    </div>
  </section>

  <section class="label label--candy">
    <p class="label__claim">Made with plant-based botanicals</p>
    <h2 class="label__title">
      <span class="label__word" style="left:44px; top:12px;">Candy</span>
      <span class="label__word" style="left:150px; top:72px;">Cane</span>
    </h2>
    <div class="label__art" role="img" aria-label="Line-art candy canes scattered in muted berry red"></div>
    <div class="label__footer">
      <span class="label__origin">Made in Canada</span><span class="label__divider"></span>
      <span class="label__brand">Wickmere Lane</span><span class="label__divider"></span>
      <span class="label__weight">Net wt. 25 oz | 709 g</span>
    </div>
  </section>

</main>
</body>
</html>
```